Need Website Design for Non-Profit Veteran Site

I am looking for a very talented creative website designer for a modern feel. I'll give a little bit of guidance around what I am looking for and then your creative juices should kick in and design away. I have already purchased the domain but will need hosting (at least temporarily) and the creative design work done.The website domain is militarydocs.orgI am looking to attract current and veteran military providers (doctors, nurse practitioners, physician assistants, etc) to join and signup for membership. They would pay a yearly fee to join. Would need membership categories $135 for Provider, $55 Student, $100 for Retired, and Organization (Organization would be broken down into Less than 100 ($200), 100-249 ($250), 250-499 ($300), 500-999 ($400), 1,000-2,999 ($500), and 3,000 ($700). Would need Benefit built out and would need to accept money through CoinLark and other means. Since it's a new organization just starting, would also need a Donate button to get people to donate if they want any amount they would like. The second part of the website is that once they join, they will have acess to a list of all other providers who have registered within the website (not exportable) so they can connect with one another. If they want to see contact information this will be included in their fee as a benefit to socialize with one another. As part of the website, there will be another Veteran's portal so veterans who would like to connect with a provider around a particular speciality can reach out and request help from the doctor writing a nexus letter or letter to support the veteran who is filing a claim with the OB. Veterans would pay a yearly sign-up fee of $30.00 and would need their membership benefits displayed. They would have access to a list of veterans in their region by state and distance, and can reach out to doctors to get their help. If a doctor and veteran agree, sharable inforamtion of medical hipaa documents can be exchanged via the website. The physician and veteran can negotiate a fee through the website only and share their details. This is a separate fee for this type of process between the provider and veteran. We will collect a $250 fee for admin on each of these and each project the veteran does with the provider will cost $450 (so essentially the doctor gets paid $450 and i get $250.00. This model could be changed over time as we start to test this out). A good example of 50% of what I'm looking for is something like the following website: https://www.qelvo.org/ It has some of the features but not all and my site should be more modernized to attract the veteran and military providers.

Target Market(s)

Current and retired military providers and veterans

Industry/Entity Type

Non Profit

Number of Pages Required

1 page

Requirements
Must have
• Military Design
• Modern Feel (Example templates for feel -https://tarnwickly.com/free-photoshop-psd-web-design-template/)
• Donation box
• Stuff mentioned in the description)
Nice to have
• Open to feedback
Should not have
• Open to feedback

```html
<!DOCTYPE html>
<html lang="en">
<head>
<meta charset="utf-8">
<title>Brenfield Care</title>
<link href="https://fonts.googleapis.com/css2?family=Open+Sans:wght@400;600;700&family=Roboto:wght@400;500;700;900&display=swap" rel="stylesheet">
<style>
:root{
  --navy:#0b5291;
  --navy-dark:#08457c;
  --red:#d71a3c;
  --sand:#e6d3b6;
  --blue:#0d5b9c;
  --sky:#5cacf0;
  --ink:#222;
  --grey:#555;
  --muted:#777;
  --line:#e4e4e4;
  --white:#fff;
}
*{box-sizing:border-box;margin:0;padding:0}
html,body{width:753px;height:1200px;overflow:hidden;background:var(--white)}
body{position:relative;font-family:"Open Sans",sans-serif;color:var(--ink)}
a{color:inherit;text-decoration:none}
.abs{position:absolute}

/* utility bar */
.utility-bar{left:0;top:0;width:753px;height:19px;background:var(--navy)}
.utility-links{left:62px;top:0;height:19px;display:flex;gap:10px;align-items:center;font-family:"Roboto",sans-serif;font-size:6.5px;color:var(--white)}
.utility-social{right:62px;top:4px;display:flex;gap:8px}
.utility-social span{width:9px;height:9px;border:1px solid var(--white);border-radius:1px;display:block}

/* header */
.brand{left:62px;top:32px;font-family:"Roboto",sans-serif;font-weight:700;font-size:21px;color:var(--navy);display:flex;align-items:center;gap:6px}
.brand-mark{width:12px;height:12px;background:var(--red)}
.search{left:322px;top:37px;width:195px;height:21px;border:1px solid #bdbdbd;font-size:7.5px;color:var(--muted);padding:0 9px;display:flex;align-items:center;justify-content:space-between}
.btn{font-family:"Roboto",sans-serif;font-weight:500;font-size:8.5px;color:var(--white);display:flex;align-items:center;justify-content:center;border-radius:2px}
.btn-donate{left:550px;top:38px;width:67px;height:20px;background:var(--red)}
.btn-join{left:623px;top:38px;width:67px;height:20px;background:var(--navy)}

/* main nav */
.main-nav{left:0;top:76px;width:753px;height:40px;border-top:1px solid var(--line);border-bottom:1px solid var(--line)}
.main-nav ul{position:absolute;left:63px;right:63px;top:0;height:39px;list-style:none;display:flex;justify-content:space-between;align-items:center;font-family:"Roboto",sans-serif;font-weight:500;font-size:7px;color:#333}

/* hero */
.hero{left:0;top:116px;width:753px;height:306px;background:linear-gradient(90deg,#e9eef0 0%,#dfe7e6 40%,#c8d8dc 60%,#e8ecee 100%)}
.hero-photo{left:380px;top:0;width:373px;height:306px;background:linear-gradient(160deg,#d8c4b4 0%,#c9a98f 35%,#3c8fd4 70%,#2f7cc2 100%);opacity:.85}
.hero-title{left:61px;top:189px;font-family:"Roboto",sans-serif;font-weight:900;font-size:21.5px;line-height:27px;color:var(--blue);letter-spacing:.2px}
.hero-sub{left:61px;top:248px;font-family:"Roboto",sans-serif;font-size:17px;color:#222}
.hero-cta{left:62px;top:282px;width:118px;height:32px;background:var(--red);font-size:13px;border-radius:2px;border:1px solid #b5132f}

/* quick actions */
.actions{left:0;top:422px;width:753px;height:80px;box-shadow:0 3px 4px rgba(0,0,0,.06)}
.action{position:absolute;top:17px;height:41px;width:152px;display:flex;align-items:center;justify-content:space-between;padding:0 13px 0 21px;font-family:"Roboto",sans-serif;font-weight:500;font-size:10px;color:var(--white);line-height:12.5px}
.action svg{width:14px;height:14px}
.action-join{left:63px;background:var(--red)}
.action-advocacy{left:221px;background:var(--sand)}
.action-ce{left:381px;background:var(--blue)}
.action-pac{left:539px;background:var(--sky)}

/* news */
.section-title{left:0;width:753px;top:524px;text-align:center;font-weight:600;font-size:16.5px;color:#444}
.news-card{position:absolute;top:568px;width:222px}
.news-image{width:222px;height:116px}
.news-body{padding:0 8px}
.news-title{margin-top:14px;font-weight:700;font-size:9.4px;line-height:12px;color:#555}
.news-meta{margin-top:7px;font-size:7px;color:var(--navy)}
.news-text{margin-top:8px;font-size:7px;line-height:9.2px;color:#666}
.news-more{margin-top:10px;display:block;font-weight:700;font-size:6.8px;color:var(--navy)}

/* footer */
.site-footer{left:0;top:878px;width:753px;height:322px;background:var(--navy);color:var(--white);font-family:"Roboto",sans-serif}
.footer-name{left:94px;top:50px;font-weight:700;font-size:12.5px}
.footer-address{left:94px;top:74px;font-size:7px}
.footer-phones{left:92px;top:91px;font-size:9px;display:flex;align-items:center;gap:6px}
.footer-social{left:599px;top:75px;display:flex;gap:6px}
.footer-social span{width:18px;height:18px;border:1px solid var(--white);display:block}
.footer-divider{left:62px;top:115px}
.footer-heading{top:153px;font-weight:700;font-size:7px}
.footer-links{top:177px;list-style:none;font-size:7px;line-height:16.2px}
.newsletter-text{left:382px;top:175px;width:300px;font-size:7px;line-height:16px}
.email-field{left:382px;top:213px;width:235px;height:26px;background:var(--white);color:#555;font-size:7.5px;display:flex;align-items:center;padding-left:15px}
.submit-btn{left:621px;top:213px;width:69px;height:26px;background:#71afd3;font-size:7.5px;display:flex;align-items:center;justify-content:center}
.copyright{left:382px;top:257px;font-size:7px}
</style>
</head>
<body>

<div class="utility-bar abs"></div>
<nav class="utility-links abs">
  <a href="#">My MD</a><a href="#">About MD</a><a href="#">Student Resources</a><a href="#">Certification</a><a href="#">International</a><a href="#">Store</a>
</nav>
<div class="utility-social abs" aria-label="Social links"><span></span><span></span><span></span><span></span></div>

<header>
  <div class="brand abs"><span class="brand-mark"></span>Brenfield Care</div>
  <div class="search abs">Search Now
    <svg width="8" height="8" viewBox="0 0 10 10"><circle cx="4" cy="4" r="3" fill="none" stroke="#0b5291" stroke-width="1.5"/><line x1="6.3" y1="6.3" x2="9" y2="9" stroke="#0b5291" stroke-width="1.5"/></svg>
  </div>
  <a class="btn btn-donate abs" href="#">Donate Now</a>
  <a class="btn btn-join abs" href="#">Join Now</a>
</header>

<nav class="main-nav abs">
  <ul>
    <li>MEMBERSHIP</li><li>EDUCATION</li><li>RESEARCH</li><li>CONFERENCES</li><li>LEGISLATION/ REGULATION</li><li>PRACTICE/ PROFESSIONAL</li><li>FELLOWS PROGRAM</li><li>PUBLICATIONS</li><li>PRESS ROOM</li>
  </ul>
</nav>

<section class="hero abs">
  <div class="hero-photo abs" role="img" aria-label="Smiling nurse in blue scrubs with a stethoscope"></div>
</section>
<h1 class="hero-title abs">PREMIER OPPORTUNITIES.<br>HIGHEST QUALITY CANDIDATES</h1>
<p class="hero-sub abs">Sign up for your personal job alert Today.</p>
<a class="btn hero-cta abs" href="#">Register Now</a>

<section class="actions abs">
  <a class="action action-join" href="#">Join/ Renew
    <svg viewBox="0 0 14 14"><rect x="3" y="4" width="8" height="9" rx="2" fill="none" stroke="#fff" stroke-width="1.5"/><rect x="5" y="1" width="4" height="3" fill="#fff"/></svg></a>
  <a class="action action-advocacy" href="#">Advocacy Center
    <svg viewBox="0 0 14 14"><circle cx="7" cy="4" r="3" fill="#fff"/><path d="M1 14c0-4 3-6 6-6s6 2 6 6z" fill="#fff"/></svg></a>
  <a class="action action-ce" href="#">CE Center
    <svg viewBox="0 0 14 14"><circle cx="3" cy="4" r="2" fill="#fff"/><circle cx="7" cy="3" r="2" fill="#fff"/><circle cx="11" cy="4" r="2" fill="#fff"/><rect x="1" y="7" width="12" height="6" rx="2" fill="#fff"/></svg></a>
  <a class="action action-pac" href="#">Political Action<br>Committee
    <svg viewBox="0 0 14 14"><path d="M7 2l2 2-2 3-2-3z" fill="#fff"/><path d="M1 6l3 6h6l3-6-2 0-2 4H6L4 6z" fill="#fff"/></svg></a>
</section>

<h2 class="section-title abs">Policy &amp; Practice News</h2>

<article class="news-card" style="left:32px">
  <div class="news-image" role="img" aria-label="Dentist treating a patient in a clinic chair" style="background:linear-gradient(135deg,#e8ecef,#9fb0bd 60%,#6f8799)"></div>
  <div class="news-body">
    <h3 class="news-title">THE STANDARD LOREM IPSUM PASSAGE FINIBUS BONORUM ET MALORUM</h3>
    <p class="news-meta">8 September, 2017, by Wren</p>
    <p class="news-text">Sed ut perspiciatis unde omnis iste natus error sit volupt accusantium doloremque laudantium, totam rem aperiam, eaque ipsa quae ab illo inventore veritatis et quasi archit beatae vitae dicta sunt explicabo.</p>
    <a class="news-more" href="#">+ READ MORE</a>
  </div>
</article>
<article class="news-card" style="left:266px">
  <div class="news-image" role="img" aria-label="Dentist showing a child a dental model" style="background:linear-gradient(135deg,#d9dce6,#c7b7a8 50%,#5b6f8c)"></div>
  <div class="news-body">
    <h3 class="news-title">THE STANDARD LOREM IPSUM PASSAGE FINIBUS BONORUM ET MALORUM</h3>
    <p class="news-meta">8 September, 2017, by Wren</p>
    <p class="news-text">Sed ut perspiciatis unde omnis iste natus error sit volupt accusantium doloremque laudantium, totam rem aperiam, eaque ipsa quae ab illo inventore veritatis et quasi archit beatae vitae dicta sunt explicabo.</p>
    <a class="news-more" href="#">+ READ MORE</a>
  </div>
</article>
<article class="news-card" style="left:499px">
  <div class="news-image" role="img" aria-label="Smiling patient in a dental chair with a dentist" style="background:linear-gradient(135deg,#2a6fb8,#d7b9a3 45%,#e9ecef)"></div>
  <div class="news-body">
    <h3 class="news-title">THE STANDARD LOREM IPSUM PASSAGE FINIBUS BONORUM ET MALORUM</h3>
    <p class="news-meta">8 September, 2017, by Wren</p>
    <p class="news-text">Sed ut perspiciatis unde omnis iste natus error sit volupt accusantium doloremque laudantium, totam rem aperiam, eaque ipsa quae ab illo inventore veritatis et quasi archit beatae vitae dicta sunt explicabo.</p>
    <a class="news-more" href="#">+ READ MORE</a>
  </div>
</article>

<footer class="site-footer abs">
  <svg class="abs" style="left:62px;top:52px" width="17" height="22" viewBox="0 0 17 22"><path d="M8.5 1a7 7 0 0 0-7 7c0 5 7 13 7 13s7-8 7-13a7 7 0 0 0-7-7z" fill="#fff"/><circle cx="8.5" cy="8" r="3" fill="#0b5291"/></svg>
  <div class="footer-name abs">Brenfield Care</div>
  <div class="footer-address abs">2280 Alder Bend Rd, Harlow, TX 77512</div>
  <div class="footer-phones abs">
    <svg width="9" height="9" viewBox="0 0 10 10"><path d="M2 1l2 2-1 1.5c.8 1.5 1.5 2.2 3 3L7.5 6l2 2-1.5 1.5C4 9 1 6 .5 1.5z" fill="#f0a43a"/></svg>000-000-0000
    <svg width="9" height="9" viewBox="0 0 10 10"><rect x="1" y="3" width="8" height="6" rx="1" fill="#f0a43a"/><rect x="3" y="1" width="4" height="3" fill="#f0a43a"/></svg>000-000-0000
  </div>
  <div class="footer-social abs" aria-label="Social links"><span></span><span></span><span></span><span></span></div>
  <svg class="footer-divider abs" width="628" height="30" viewBox="0 0 628 30">
    <path d="M0 13H258l4-12 5 26 4-14H628" fill="none" stroke="#fff" stroke-width=".8" stroke-dasharray="2 2"/>
  </svg>

  <div class="footer-heading abs" style="left:64px">Quick Links</div>
  <ul class="footer-links abs" style="left:64px"><li>SERVICES</li><li>BILLING</li><li>CAREERS</li><li>STATE REGULATIONS</li><li>BLOG</li><li>CONTACT</li></ul>
  <div class="footer-heading abs" style="left:220px">Quick Links</div>
  <ul class="footer-links abs" style="left:223px"><li>SERVICES</li><li>BILLING</li><li>CAREERS</li><li>STATE REGULATIONS</li><li>BLOG</li><li>CONTACT</li></ul>

  <div class="footer-heading abs" style="left:380px">Subscribe The Newsletter</div>
  <p class="newsletter-text abs">Subscribe to our newsletter and stay updated on the latest news. We will keep you informed about special offers.</p>
  <div class="email-field abs">Email Address*</div>
  <div class="submit-btn abs">Submit</div>
  <div class="copyright abs">Copyright © 2017 Website</div>
</footer>

</body>
</html>
```